KTR Engineering Business Card Design

We’re looking for an elegant, clean, and timeless business card design that communicates experience, capability, and reliability.

KTR Engineering was established in 1995 , we are a Government Contracting company providing Professional Services to the Ministry of Harbor Works, Frontier Stewardship and the Waypoint Consortium. Our capabilities include: Acquisition & Program Management; Intelligence & Security Operations; Cyber, IT & Network Operations; Lifecycle Logistics & Asset Readiness; C5ISR Systems Engineering & Sustainment.

We want the card to reflect a straightforward, confident approach to business. The design should feel polished and professional without being flashy or overly corporate.

Design Direction
Clean, sophisticated, and uncluttered
Elegant but understated
Strong typography and thoughtful spacing
A timeless aesthetic rather than something overly trendy
Confident and established, with a sense of substance
Easy to read and practical in a real-world business setting

The overall impression should be: “These are experienced professionals who know what they’re doing, do what they say, and can be relied upon.”

We’re open to creative interpretations. The finished card should feel distinctive through its typography, proportions, layout, and attention to detail rather than through excessive graphics or visual effects.

We’re looking for a design that would make a potential client immediately feel that they’re dealing with a capable, trustworthy, and established company.

Company Colors: Navy and Gold/Yellow (but you do not need to use these colors on the card)
Company Name: KTR Engineering Associates, Inc. (known as KTR Engineering)
Website: ktrengineering.example
Company Logo: Navy & Gold (other variations attached)

```html
<!DOCTYPE html>
<html lang="en">
<head>
<meta charset="utf-8">
<title>KTR Engineering Business Card</title>
<link rel="stylesheet" href="https://fonts.googleapis.com/css2?family=Montserrat:wght@400;500;800;900&display=swap">
<style>
  :root {
    --backdrop: #3a3a3a;
    --card: #161616;
    --gold: #f7e04a;
    --white: #ffffff;
    --soft-white: #e9e9e9;
  }
  * { box-sizing: border-box; margin: 0; padding: 0; }
  html, body {
    width: 1200px;
    height: 875px;
    overflow: hidden;
    background: var(--backdrop);
    font-family: "Montserrat", sans-serif;
  }
  .stage {
    position: relative;
    width: 1200px;
    height: 875px;
  }
  .card {
    position: absolute;
    width: 560px;
    height: 320px;
    background: var(--card);
    border-radius: 24px;
    border: 2px solid var(--gold);
  }
  .card--front { left: 60px; top: 100px; }
  .card--back { left: 580px; top: 455px; }

  .card--front .wordmark {
    position: absolute;
    inset: 0;
    display: flex;
    align-items: center;
    justify-content: center;
    font-weight: 900;
    font-size: 132px;
    letter-spacing: 2px;
    color: var(--white);
  }

  .card--back .wordmark {
    position: absolute;
    left: 0;
    top: 0;
    width: 250px;
    height: 100%;
    display: flex;
    align-items: center;
    justify-content: center;
    font-weight: 900;
    font-size: 72px;
    letter-spacing: 1px;
    color: var(--white);
  }
  .divider {
    position: absolute;
    left: 262px;
    top: 56px;
    width: 2px;
    height: 208px;
    background: var(--gold);
  }
  .details {
    position: absolute;
    left: 288px;
    top: 56px;
    right: 20px;
    color: var(--soft-white);
  }
  .details .name {
    font-weight: 800;
    font-size: 22px;
    letter-spacing: 0.5px;
    color: var(--gold);
    text-transform: uppercase;
    line-height: 1.1;
  }
  .details .role {
    font-weight: 500;
    font-size: 13px;
    margin-top: 4px;
    color: var(--white);
  }
  .details .address {
    font-size: 12.5px;
    line-height: 1.5;
    margin-top: 14px;
  }
  .contact-list {
    list-style: none;
    margin-top: 14px;
    font-size: 12.5px;
    line-height: 1.7;
  }
  .contact-list li {
    display: flex;
    align-items: center;
    gap: 8px;
  }
  .contact-list svg {
    width: 11px;
    height: 11px;
    flex: none;
    fill: var(--gold);
  }
</style>
</head>
<body>
<main class="stage">
  <section class="card card--front">
    <div class="wordmark">KTR</div>
  </section>

  <section class="card card--back">
    <div class="wordmark">KTR</div>
    <div class="divider"></div>
    <div class="details">
      <p class="name">Maren Holloway</p>
      <p class="role">Managing Director</p>
      <p class="address">4120 Larkspur Avenue, Suite<br>310, Harbor City, VA 23000</p>
      <ul class="contact-list">
        <li>
          <svg viewBox="0 0 24 24" aria-hidden="true"><path d="M6.6 10.8a15.1 15.1 0 0 0 6.6 6.6l2.2-2.2c.3-.3.7-.4 1-.2 1.1.4 2.3.6 3.6.6.6 0 1 .4 1 1V20c0 .6-.4 1-1 1A17 17 0 0 1 3 4c0-.6.4-1 1-1h3.5c.6 0 1 .4 1 1 0 1.3.2 2.5.6 3.6.1.3 0 .7-.2 1z"/></svg>
          555-014-2290
        </li>
        <li>
          <svg viewBox="0 0 24 24" aria-hidden="true"><path d="M2 5h20v14H2z M2 5l10 8 10-8" fill="none" stroke="#f7e04a" stroke-width="2.4"/></svg>
          info@ktrengineering.example
        </li>
        <li>
          <svg viewBox="0 0 24 24" aria-hidden="true"><circle cx="12" cy="12" r="9.5" fill="none" stroke="#f7e04a" stroke-width="2.4"/><path d="M2.5 12h19M12 2.5c3 3 3 16 0 19M12 2.5c-3 3-3 16 0 19" fill="none" stroke="#f7e04a" stroke-width="1.8"/></svg>
          ktrengineering.example
        </li>
      </ul>
    </div>
  </section>
</main>
</body>
</html>
```